Medical Billing Company Needs a Business Card Design

We need a business card design for a Florida based medical billing company called 'Lorrimer Tallbrook Services'. We specialize in providing revenue cycle management services to physician and therapist offices (we're basically their back-office processing partner for providing billing software, claims submissions, A/R follow-up and patient statements & collections. Our logo is red and blue-ish, so make sure that whatever other elements are used will match appropriately. Our current business card design has a too small font size. I'd like to project an image that shows we are modern & reliable. On a side note, I'm planning on using VUX for printing these cards.

Target Market(s)

Office managers, physicians, therapists

Industry/Entity Type

Printing

Requirements
Must have
• Logo
Name of Employee
Phone
Fax
E-mail
Website

```html
<!DOCTYPE html>
<html lang="en">
<head>
<meta charset="utf-8">
<title>Lorrimer Tallbrook Services – Business Card</title>
<link href="https://fonts.googleapis.com/css2?family=Lato:wght@400;700&display=swap" rel="stylesheet">
<style>
  :root {
    --navy: #2c2a7e;
    --red: #9a1d27;
    --ink: #3a3a3a;
    --paper: #ffffff;
    --backdrop: #ececec;
  }
  * { margin: 0; padding: 0; box-sizing: border-box; }
  html, body {
    width: 1200px; height: 1000px; overflow: hidden;
    background: var(--backdrop);
    font-family: "Lato", Arial, sans-serif;
  }
  .canvas {
    width: 1200px; height: 1000px;
    display: flex; flex-direction: column;
    align-items: center; justify-content: center; gap: 70px;
  }
  .card {
    position: relative;
    width: 560px; height: 320px;
    background: var(--paper);
    box-shadow: 0 2px 10px rgba(0,0,0,0.08);
    overflow: hidden;
  }
  .card::after {
    content: ""; position: absolute; left: 0; right: 0; bottom: 0;
    height: 3px; background: var(--red);
  }

  /* Front side */
  .front .brand-tag {
    position: absolute; top: 30px; right: 34px;
    display: flex; align-items: center; gap: 8px;
    font-weight: 700; font-size: 13px; letter-spacing: 1.5px;
    color: var(--navy);
  }
  .brand-square { width: 14px; height: 14px; background: var(--red); }
  .front .identity { position: absolute; left: 42px; top: 92px; }
  .employee-name { font-weight: 700; font-size: 26px; color: var(--navy); line-height: 1.1; }
  .employee-title { font-size: 13px; letter-spacing: 0.6px; color: var(--ink); margin-top: 4px; }
  .contact { position: absolute; left: 42px; top: 182px; font-size: 15px; color: var(--ink); line-height: 1.35; }
  .contact .label { color: var(--navy); display: inline-block; width: 14px; }
  .contact .address { padding-left: 14px; }
  .front .rule-blue {
    position: absolute; left: 0; right: 0; bottom: 22px;
    height: 2px; background: var(--navy);
  }

  /* Back side */
  .back .wordmark {
    position: absolute; left: 0; right: 0; top: 110px;
    display: flex; align-items: center; justify-content: center; gap: 12px;
    font-weight: 400; font-size: 34px; letter-spacing: 3px;
    color: var(--navy);
  }
  .back .wordmark .brand-square { width: 20px; height: 20px; }
  .back .rule-top {
    position: absolute; right: 0; top: 196px;
    width: 110px; height: 2px; background: var(--navy);
  }
  .back .web-row {
    position: absolute; left: 0; right: 0; bottom: 30px;
    display: flex; align-items: center; gap: 16px;
  }
  .back .web-row .line { flex: 1; height: 2px; background: var(--navy); }
  .back .web-row .line.short { flex: 0 0 70px; }
  .web { font-size: 15px; color: var(--navy); }
</style>
</head>
<body>
<main class="canvas">
  <section class="card front" aria-label="Business card front">
    <div class="brand-tag"><span class="brand-square"></span>LORRIMER TALLBROOK</div>
    <div class="identity">
      <p class="employee-name">Dorian Vale</p>
      <p class="employee-title">CONSULTANT &amp; EDUCATOR</p>
    </div>
    <div class="contact">
      <p><span class="label">t</span> 800 555 0142</p>
      <p><span class="label">e</span> info@lorrimertallbrook.net</p>
      <p class="address">2780 SW Harbor Lane</p>
      <p class="address">Port Kessel, FL 34000</p>
    </div>
    <div class="rule-blue"></div>
  </section>

  <section class="card back" aria-label="Business card back">
    <div class="wordmark"><span>LORRIMER TALLBROOK</span><span class="brand-square"></span></div>
    <div class="rule-top"></div>
    <div class="web-row">
      <span class="line"></span>
      <span class="web">www.lorrimertallbrook.net</span>
      <span class="line short"></span>
    </div>
  </section>
</main>
</body>
</html>
```